After tattoo calming solution

The label has to be modern, along the same lines as skin care brand “Dew Harbor.” It has to reflect the solutions natural effectiveness and simplicity. The label cannot be over fussy, and must be a little bit clinical, as it really does work. The colours should reflect that the solution calms the skin.

We use a 100ml spray bottle.

Target Market(s)

Anyone with a new tattoo or piercing

Industry/Entity Type

Skincare

Requirements
Must have
• Must reflect its natural calming but still remain a little clinical
Should not have
• It must not look like other flowery tattoo cream solutions.

```html
<!DOCTYPE html>
<html lang="en">
<head>
<meta charset="utf-8">
<title>After Tattoo &amp; Piercing – Label</title>
<link rel="stylesheet" href="https://fonts.googleapis.com/css2?family=Marcellus&family=Bellefair&display=swap">
<style>
  :root {
    --backdrop: #636e79;
    --label-white: #ffffff;
    --calm-blue: #c2dcf6;
    --ink-navy: #1f2f8c;
    --ink-dark: #1b1b1b;
  }
  * { margin: 0; padding: 0; box-sizing: border-box; }
  html, body {
    width: 1200px;
    height: 766px;
    overflow: hidden;
    background: var(--backdrop);
  }
  .canvas {
    position: relative;
    width: 1200px;
    height: 766px;
    background: var(--backdrop);
  }
  .label {
    position: absolute;
    left: 397px;
    top: 35px;
    width: 406px;
    height: 695px;
    background: var(--label-white);
    box-shadow: 0 6px 18px rgba(0, 0, 0, 0.35);
    overflow: hidden;
  }
  .brand {
    position: absolute;
    left: 0;
    top: 140px;
    width: 100%;
    display: flex;
    align-items: center;
    justify-content: center;
    gap: 12px;
  }
  .brand-dot {
    width: 34px;
    height: 34px;
    border-radius: 50%;
    background: var(--calm-blue);
  }
  .brand-name {
    font-family: "Marcellus", serif;
    font-size: 34px;
    color: var(--ink-navy);
    letter-spacing: 1px;
  }
  .product-title {
    position: absolute;
    left: 75px;
    top: 290px;
    font-family: "Marcellus", serif;
    font-weight: 400;
    color: var(--ink-navy);
    line-height: 1;
  }
  .product-title .main {
    display: block;
    font-size: 37px;
    letter-spacing: 0.5px;
  }
  .product-title .sub {
    display: block;
    margin-top: 4px;
    font-size: 24px;
  }
  .benefits {
    position: absolute;
    left: 75px;
    top: 366px;
    width: 280px;
    font-family: "Bellefair", serif;
    font-size: 20px;
    line-height: 22px;
    color: var(--ink-dark);
  }
  .claim-panel {
    position: absolute;
    left: 50px;
    top: 452px;
    width: 304px;
    height: 243px;
    background: var(--calm-blue);
  }
  .claim {
    position: absolute;
    left: 25px;
    top: 26px;
    font-family: "Marcellus", serif;
    font-size: 30px;
    line-height: 31px;
    color: var(--ink-navy);
  }
  .volume {
    position: absolute;
    left: 0;
    top: 186px;
    width: 100%;
    text-align: center;
    font-family: "Bellefair", serif;
    font-size: 21px;
    color: var(--ink-dark);
  }
</style>
</head>
<body>
  <main class="canvas">
    <section class="label">
      <div class="brand">
        <span class="brand-dot"></span>
        <span class="brand-name">Dew Harbor</span>
      </div>
      <h1 class="product-title">
        <span class="main">AFTER TATTOO</span>
        <span class="sub">&amp; PIERCING</span>
      </h1>
      <p class="benefits">Reduces inflammation, irritation andencourages natural skin healing</p>
      <div class="claim-panel">
        <p class="claim">Expert skin repair<br>for new tattoos<br>&amp; piercings</p>
        <p class="volume">100ml e 3.3 fl oz</p>
      </div>
    </section>
  </main>
</body>
</html>
```